Business Coach needs an elegant business card design

I need a business card design based around my logo for color and to look like a millionaire dollar coach. Incorporate the color of my logo with something creative and attractive that stands out. I am focused on high end companies and the card must look and feel that way.

Target Market(s)

High End Companies and Business Owners - Training People to become millionaires

Industry/Entity Type

Business

Requirements
Must have
• Front -
Logo (attached file) - Website (marlowkeeve.com) - Name (Marlow Keeve) Phone (555.201.7746) - Email (marlow@marlowkeeve.com) (My Title - Success Coach)
Back -
Slogan - Vision (see it) . Action (do it) . Transformation (be it)
Website - Learn More @ marlowkeeve.com

Creative High End Look!
Nice to have
Should not have
• Cheap standard look
nothing traditional

```html
<!DOCTYPE html>
<html lang="en">
<head>
<meta charset="utf-8">
<title>Marlow Keeve Coaching – Business Card</title>
<link rel="stylesheet" href="https://fonts.googleapis.com/css2?family=Cinzel:wght@500;700&family=Noto+Serif:ital,wght@0,400;0,700;1,400&display=swap">
<style>
  :root {
    --navy: #1f2d5c;
    --grey-text: #6f6f73;
    --rule: #7d7f86;
    --card: #ffffff;
    --card-tint: #f3f4f7;
    --faint: #e4e6ec;
    --backdrop: #d9d9db;
    --photo-dark: #3c3f44;
    --photo-light: #8d9096;
  }
  * { margin: 0; padding: 0; box-sizing: border-box; }
  html, body { width: 1200px; height: 914px; overflow: hidden; }
  body {
    background: var(--backdrop);
    font-family: "Noto Serif", Georgia, serif;
    position: relative;
  }
  .card {
    position: absolute;
    width: 560px;
    height: 320px;
    background: var(--card);
    box-shadow: 0 6px 18px rgba(0,0,0,0.18);
    overflow: hidden;
  }

  /* Back card */
  .card-back { left: 580px; top: 110px; }
  .portrait {
    position: absolute;
    left: 20px; top: 30px;
    width: 190px; height: 290px;
    background: linear-gradient(180deg, var(--photo-light) 0%, var(--photo-dark) 55%, #2b2d31 100%);
    border-radius: 95px 95px 0 0;
  }
  .quote-block {
    position: absolute;
    right: 26px; top: 108px;
    width: 296px;
    text-align: right;
    color: var(--navy);
  }
  .quote {
    font-style: italic;
    font-size: 13px;
    line-height: 1.5;
  }
  .quote-author {
    margin-top: 10px;
    font-weight: 700;
    font-size: 14px;
    letter-spacing: 0.5px;
  }
  .learn-more {
    margin-top: 12px;
    font-size: 13.5px;
  }

  /* Front card */
  .card-front { left: 60px; top: 480px; background: linear-gradient(90deg, var(--card-tint) 0%, var(--card) 55%); }
  .backdrop-rings { position: absolute; left: -110px; top: -120px; }
  .brand {
    position: absolute;
    left: 30px; top: 150px;
    display: flex;
    align-items: center;
    gap: 14px;
  }
  .brand-dot {
    width: 70px; height: 70px;
    border-radius: 50%;
    background: var(--navy);
    flex: none;
  }
  .brand-name {
    font-family: "Cinzel", "Times New Roman", serif;
    font-weight: 500;
    color: var(--navy);
    font-size: 30px;
    line-height: 1.05;
    letter-spacing: 1px;
  }
  .brand-sub {
    display: flex;
    align-items: center;
    gap: 10px;
    margin-top: 2px;
    font-size: 17px;
    letter-spacing: 6px;
  }
  .brand-sub span { margin-right: -6px; }
  .brand-sub::before,
  .brand-sub::after {
    content: "";
    flex: 1;
    height: 2px;
    background: var(--rule);
  }
  .identity {
    position: absolute;
    right: 40px; top: 70px;
    text-align: right;
  }
  .identity-name {
    font-family: "Cinzel", "Times New Roman", serif;
    font-weight: 500;
    color: var(--navy);
    font-size: 24px;
    letter-spacing: 0.5px;
  }
  .identity-title {
    color: var(--grey-text);
    font-size: 14px;
    letter-spacing: 1px;
  }
  .contact {
    position: absolute;
    right: 36px; bottom: 36px;
    list-style: none;
    color: var(--grey-text);
    font-size: 14px;
  }
  .contact li {
    display: flex;
    justify-content: flex-end;
    align-items: center;
    gap: 10px;
    line-height: 1.55;
  }
  .contact svg { width: 12px; height: 12px; fill: var(--navy); }
</style>
</head>
<body>

<section class="card card-back" aria-label="Card back">
  <div class="portrait" role="img" aria-label="Portrait photograph of the coach in a dark blazer"></div>
  <div class="quote-block">
    <p class="quote">"You have a defined purpose in life and business. I have a passion to help you See it, Embrace it, and Live it!"</p>
    <p class="quote-author">- MARLOW KEEVE</p>
    <p class="learn-more">Learn More @ marlowkeeve.com</p>
  </div>
</section>

<section class="card card-front" aria-label="Card front">
  <svg class="backdrop-rings" width="420" height="420" viewBox="0 0 420 420" aria-hidden="true">
    <circle cx="210" cy="210" r="190" fill="none" stroke="var(--faint)" stroke-width="14"/>
    <circle cx="210" cy="210" r="160" fill="var(--faint)" opacity="0.6"/>
  </svg>

  <div class="brand">
    <span class="brand-dot"></span>
    <div class="brand-name">
      <p>MARLOW KEEVE</p>
      <p class="brand-sub"><span>COACHING</span></p>
    </div>
  </div>

  <div class="identity">
    <p class="identity-name">MARLOW KEEVE</p>
    <p class="identity-title">Success Coach</p>
  </div>

  <ul class="contact">
    <li>555.201.7746
      <svg viewBox="0 0 12 12"><circle cx="6" cy="3.5" r="2.6"/><path d="M1 12c0-3 2.2-5 5-5s5 2 5 5z"/></svg>
    </li>
    <li>marlowkeeve.com
      <svg viewBox="0 0 12 12"><circle cx="6" cy="6" r="5.5"/><path d="M0.5 6h11M6 0.5c2 2 2 9 0 11M6 0.5c-2 2-2 9 0 11" stroke="#fff" stroke-width="0.8" fill="none"/></svg>
    </li>
    <li>marlow@marlowkeeve.com
      <svg viewBox="0 0 12 12"><rect x="0.5" y="2" width="11" height="8"/><path d="M0.5 2l5.5 4.5 5.5-4.5" stroke="#fff" stroke-width="0.9" fill="none"/></svg>
    </li>
  </ul>
</section>

</body>
</html>
```